Marlow Realty Real Estate Brokerage Recruiting Flyer

We are a real estate brokerage looking to hire more real estate agents. We need to list everything we have to offer as a company so real estate agents will join our company. this is our company website: www.Marlowrealty.example .

100% COMMISSION NO MONTHLY FEE
$450 Flat Transaction FEE

What We Offer:
24/7 Office Access
Free E & O Insurance for 1st Year
Free Online CE and PLE
Free 1,000 Business Cards
Free Professional Social Media Marketing
Free Printing, Scanning, and Copies
Free Buyer and Seller Presentation Packages
Free Filquay Cloud Based Document Management Access
Access to our Internal Brokerage Forum
Company Profit Sharing!
Private Offices Available to Rent

*Lead Generation Software with over 3,000 Leads
*10 Leads to Start
* Free Personal CRM and Website
*Restrictions and Rules apply

Company Address:
4817 Amberfield Road
Suite 512
Fairfax, VA 22194
Phone: 703-555-0147
email: info@marlowrealty.example

Target Market(s)

Real Estate Agents

Industry/Entity Type

Real Estate

Colors
0555a3
ffffff

Requirements
Must have
• 100% COMMISSION NO MONTHLY FEE
$450 Flat Transaction FEE

What We Offer:
24/7 Office Access
Free Online CE and PLE
Free 1,000 Business Cards
Company Profit Sharing!

*10 Leads to Start

Company Address:
4817 Amberfield Road
Suite 512
Fairfax, VA 22194
Phone: 703-555-0147

```html
<!DOCTYPE html>
<html lang="en">
<head>
<meta charset="utf-8">
<title>Marlow Realty – Agent Recruiting Flyer</title>
<link rel="stylesheet" href="https://fonts.googleapis.com/css2?family=Montserrat:wght@400;500;600;700;900&family=Oswald:wght@500;600;700&display=swap">
<style>
  :root {
    --brand-blue: #0555a3;
    --mid-blue: #1a66bd;
    --deep-blue: #0b3f86;
    --list-blue: #2d6cbc;
    --headline-navy: #0d4ea3;
    --orange: #f7931e;
    --white: #ffffff;
    --footer-grey: #e4e6ea;
    --stage: #ebe8e3;
  }
  * { margin: 0; padding: 0; box-sizing: border-box; }
  html, body { width: 1200px; height: 979px; overflow: hidden; }
  body { background: var(--stage); position: relative; font-family: "Montserrat", sans-serif; }

  .flyer {
    position: absolute; left: 255px; top: 20px;
    width: 690px; height: 940px;
    background: var(--white);
    box-shadow: 0 4px 18px rgba(0,0,0,.18);
    overflow: hidden;
  }
  .flyer-shapes { position: absolute; inset: 0; }
  .abs { position: absolute; }

  .brand {
    left: 28px; top: 48px; display: flex; align-items: center; gap: 10px;
    font-family: "Montserrat", sans-serif; font-weight: 600; font-size: 30px;
    color: var(--headline-navy); letter-spacing: 1px;
  }
  .brand-mark { width: 22px; height: 22px; background: var(--headline-navy); }

  .headline { left: 27px; top: 258px; transform: translateY(-100%); color: var(--headline-navy); line-height: 1.12; }
  .headline-strong { font-weight: 900; font-size: 30px; display: block; }
  .headline-light { font-weight: 400; font-size: 25px; display: block; letter-spacing: .5px; margin-top: 4px; }

  .fee-block { left: 0; top: 318px; width: 315px; text-align: center; color: var(--white); font-family: "Oswald", sans-serif; }
  .fee-note { font-weight: 600; font-size: 18px; letter-spacing: .3px; display: block; }
  .fee-amount { font-weight: 700; font-size: 28px; line-height: 1; display: block; margin-top: 8px; }
  .fee-label { font-weight: 700; font-size: 24px; line-height: 1.1; display: block; }

  .leads-block { left: 338px; top: 306px; color: var(--white); }
  .leads-title { font-family: "Oswald", sans-serif; font-weight: 600; font-size: 24px; line-height: 1.2; padding-left: 12px; }
  .leads-rule { width: 292px; height: 2px; background: var(--white); margin: 10px 0 11px 4px; }
  .leads-points { list-style: none; font-weight: 600; font-size: 13.5px; line-height: 1.6; }

  .perk-column { left: 0; top: 420px; width: 213px; height: 450px; color: var(--white); font-family: "Oswald", sans-serif; }
  .perk-commission { position: absolute; left: 30px; top: 60px; }
  .perk-big { font-weight: 700; font-size: 56px; line-height: 1; display: block; }
  .perk-sub { font-weight: 600; font-size: 29px; line-height: 1.1; display: block; margin-top: 4px; }
  .perk-nofee { position: absolute; left: 36px; top: 194px; font-weight: 600; font-size: 37px; line-height: 1.12; }
  .licensed { position: absolute; left: 42px; top: 364px; font-family: "Montserrat", sans-serif; font-weight: 400; font-size: 12px; line-height: 1.4; letter-spacing: .3px; }

  .offer { left: 239px; top: 476px; }
  .offer-title { font-family: "Montserrat", sans-serif; font-weight: 900; font-size: 34px; color: var(--orange); letter-spacing: .3px; line-height: 1; }
  .offer-list { list-style: none; margin-top: 15px; }
  .offer-item {
    display: flex; align-items: center; gap: 11px; height: 30.2px;
    font-family: "Oswald", sans-serif; font-weight: 500; font-size: 15.5px; color: var(--list-blue);
  }
  .tick { width: 15px; height: 15px; flex: none; }

  .contact { top: 870px; left: 0; width: 690px; height: 70px; color: var(--list-blue); font-weight: 600; }
  .contact-item { position: absolute; top: 50%; transform: translateY(-50%); display: flex; align-items: center; gap: 10px; white-space: nowrap; }
  .contact-address { left: 40px; font-size: 11.5px; line-height: 1.35; }
  .contact-phone { left: 294px; font-size: 14px; }
  .contact-email { right: 30px; font-size: 13px; font-weight: 500; }
  .icon { flex: none; fill: var(--list-blue); }
</style>
</head>
<body>
<main class="flyer">
  <svg class="flyer-shapes" width="690" height="940" viewBox="0 0 690 940">
    <defs>
      <linearGradient id="photoTone" x1="0" y1="0" x2="1" y2="1">
        <stop offset="0" stop-color="#e6eef6"/>
        <stop offset=".55" stop-color="#b9c8d8"/>
        <stop offset="1" stop-color="#2a3344"/>
      </linearGradient>
      <linearGradient id="columnTone" x1="0" y1="0" x2="0" y2="1">
        <stop offset="0" stop-color="#1763b8"/>
        <stop offset="1" stop-color="#5a8fcd"/>
      </linearGradient>
    </defs>
    <polygon role="img" aria-label="Photo of three smiling real estate agents in business suits" points="362,0 690,0 690,300 302,310" fill="url(#photoTone)"/>
    <polygon points="0,310 315,310 303,420 0,420" fill="var(--orange)"/>
    <polygon points="258,420 290,420 290,456" fill="var(--deep-blue)"/>
    <polygon points="316,295 690,295 690,456 288,456" fill="var(--mid-blue)"/>
    <rect x="0" y="420" width="213" height="450" fill="url(#columnTone)"/>
    <rect x="0" y="870" width="690" height="70" fill="var(--footer-grey)"/>
  </svg>

  <div class="abs brand"><span class="brand-mark"></span>Marlow Realty</div>

  <h1 class="abs headline">
    <span class="headline-strong">JOIN OUR</span>
    <span class="headline-strong">WINNING TEAM</span>
    <span class="headline-light">OF AGENTS TODAY!</span>
  </h1>

  <div class="abs fee-block">
    <span class="fee-note">RESTRICTIONS AND RULES APPLY</span>
    <span class="fee-amount">$450 FLAT</span>
    <span class="fee-label">TRANSACTION FEE</span>
  </div>

  <div class="abs leads-block">
    <div class="leads-title">LEAD GENERATION SOFTWARE<br>WITH OVER 3,000 LEADS</div>
    <div class="leads-rule"></div>
    <ul class="leads-points">
      <li>- 10 LEADS TO START</li>
      <li>- FREE PERSONAL CRM AND WEBSITE</li>
    </ul>
  </div>

  <div class="abs perk-column">
    <div class="perk-commission">
      <span class="perk-big">100%</span>
      <span class="perk-sub">COMMISSION</span>
    </div>
    <div class="perk-nofee">NO<br>MONTHLY<br>FEE</div>
    <p class="licensed">LICENSED IN<br>D.C., MARYLAND,<br>AND VIRGINIA</p>
  </div>

  <section class="abs offer">
    <h2 class="offer-title">WHAT WE OFFER</h2>
    <ul class="offer-list">
      <li class="offer-item"><svg class="tick" viewBox="0 0 16 16"><rect x="1" y="3" width="12" height="12" fill="none" stroke="#2d6cbc" stroke-width="1.6"/><path d="M4 8.5 7 11.5 15 2.5" fill="none" stroke="#2d6cbc" stroke-width="1.8"/></svg>24/7 OFFICE ACCESS</li>
      <li class="offer-item"><svg class="tick" viewBox="0 0 16 16"><rect x="1" y="3" width="12" height="12" fill="none" stroke="#2d6cbc" stroke-width="1.6"/><path d="M4 8.5 7 11.5 15 2.5" fill="none" stroke="#2d6cbc" stroke-width="1.8"/></svg>FREE E &amp; O INSURANCE OR 1ST YEAR</li>
      <li class="offer-item"><svg class="tick" viewBox="0 0 16 16"><rect x="1" y="3" width="12" height="12" fill="none" stroke="#2d6cbc" stroke-width="1.6"/><path d="M4 8.5 7 11.5 15 2.5" fill="none" stroke="#2d6cbc" stroke-width="1.8"/></svg>FREE ONLINE CE AND PLE</li>
      <li class="offer-item"><svg class="tick" viewBox="0 0 16 16"><rect x="1" y="3" width="12" height="12" fill="none" stroke="#2d6cbc" stroke-width="1.6"/><path d="M4 8.5 7 11.5 15 2.5" fill="none" stroke="#2d6cbc" stroke-width="1.8"/></svg>FREE 1,000 BUSINESS CARDS</li>
      <li class="offer-item"><svg class="tick" viewBox="0 0 16 16"><rect x="1" y="3" width="12" height="12" fill="none" stroke="#2d6cbc" stroke-width="1.6"/><path d="M4 8.5 7 11.5 15 2.5" fill="none" stroke="#2d6cbc" stroke-width="1.8"/></svg>FREE PROFESSIONAL SOCIAL MEDIA MARKETING</li>
      <li class="offer-item"><svg class="tick" viewBox="0 0 16 16"><rect x="1" y="3" width="12" height="12" fill="none" stroke="#2d6cbc" stroke-width="1.6"/><path d="M4 8.5 7 11.5 15 2.5" fill="none" stroke="#2d6cbc" stroke-width="1.8"/></svg>FREE PRINTING, SCANNING, AND COPIES</li>
      <li class="offer-item"><svg class="tick" viewBox="0 0 16 16"><rect x="1" y="3" width="12" height="12" fill="none" stroke="#2d6cbc" stroke-width="1.6"/><path d="M4 8.5 7 11.5 15 2.5" fill="none" stroke="#2d6cbc" stroke-width="1.8"/></svg>FREE BUYER AND SELLER PRESENTATION PACKAGES</li>
      <li class="offer-item"><svg class="tick" viewBox="0 0 16 16"><rect x="1" y="3" width="12" height="12" fill="none" stroke="#2d6cbc" stroke-width="1.6"/><path d="M4 8.5 7 11.5 15 2.5" fill="none" stroke="#2d6cbc" stroke-width="1.8"/></svg>FREE FILQUAY CLOUD BASED DOCUMENT MANAGEMENT ACCESS</li>
      <li class="offer-item"><svg class="tick" viewBox="0 0 16 16"><rect x="1" y="3" width="12" height="12" fill="none" stroke="#2d6cbc" stroke-width="1.6"/><path d="M4 8.5 7 11.5 15 2.5" fill="none" stroke="#2d6cbc" stroke-width="1.8"/></svg>ACCESS TO OUR INTERNAL BROKERAGE FORUM</li>
      <li class="offer-item"><svg class="tick" viewBox="0 0 16 16"><rect x="1" y="3" width="12" height="12" fill="none" stroke="#2d6cbc" stroke-width="1.6"/><path d="M4 8.5 7 11.5 15 2.5" fill="none" stroke="#2d6cbc" stroke-width="1.8"/></svg>COMPANY PROFIT SHARING!</li>
      <li class="offer-item"><svg class="tick" viewBox="0 0 16 16"><rect x="1" y="3" width="12" height="12" fill="none" stroke="#2d6cbc" stroke-width="1.6"/><path d="M4 8.5 7 11.5 15 2.5" fill="none" stroke="#2d6cbc" stroke-width="1.8"/></svg>PRIVATE OFFICES AVAILABLE TO RENT</li>
    </ul>
  </section>

  <footer class="abs contact">
    <div class="contact-item contact-address">
      <svg class="icon" width="12" height="16" viewBox="0 0 12 16"><path d="M6 0C2.7 0 0 2.6 0 5.9 0 10.3 6 16 6 16s6-5.7 6-10.1C12 2.6 9.3 0 6 0zm0 8.2A2.3 2.3 0 1 1 6 3.6a2.3 2.3 0 0 1 0 4.6z"/></svg>
      <span>4817 AMBERFIELD ROAD,<br>SUITE 512, FAIRFAX, VA 22194</span>
    </div>
    <div class="contact-item contact-phone">
      <svg class="icon" width="13" height="16" viewBox="0 0 13 16"><path d="M3.2 0 5.4 3.9 3.9 5.6c.6 2 1.9 3.9 3.6 5.2l1.8-1.2 3.2 3.1-1.7 2.7C5 14.8.9 8.3 1 1.6z"/></svg>
      <span>703-555-0147</span>
    </div>
    <div class="contact-item contact-email">
      <svg class="icon" width="20" height="14" viewBox="0 0 20 14"><path d="M0 0h20v1.5L10 8 0 1.5z"/><path d="M0 3.6 10 10l10-6.4V14H0z"/></svg>
      <span>info@marlowrealty.example</span>
    </div>
  </footer>
</main>
</body>
</html>
```